Word Template for Communications, Reports

I. A Word template for External Reports and a Word template for External Communications
1.Create a template in Word for reports and another template in Word for sending external communications.
1.1. Predefined and locked text styles.
1.2. Quick elements fields (custom) that allow the integration of basic information of each document.
1.3. Professional design and that administrators can place it to different projects.

II. Job postings
We also want a template in Word to make vacancy postings, to facilitate the job of recruiting staff.
Updates

Target Market(s)

External clients (our main clients are public institutions of the government of the Dominican Republic.)

Industry/Entity Type

Construcción

Font styles to use
Serif
Other font styles liked:
• Arial, Book Antiqua

Colors
EE7325
F08F49
F5BC92
FAE3D3
FDF4ED
EB3D1F
EC4F4E
F09395
F8D3D4
FCEDEE

Requirements
Nice to have
• Since we are a group of about 4 companies, I would like each template to be used by any of the companies

```html
<!DOCTYPE html>
<html lang="en">
<head>
<meta charset="utf-8">
<title>Annual Report 2022 – Arven</title>
<link rel="stylesheet" href="https://fonts.googleapis.com/css2?family=League+Spartan:wght@400;500;600;700;800&family=Open+Sans:wght@400;600&display=swap">
<style>
:root{
  --backdrop:#808080;
  --paper:#ffffff;
  --red:#ed1c24;
  --ink:#111111;
  --charcoal:#1e1e1e;
  --maroon:#b3182a;
  --ring:#d9d9d9;
  --text:#2a2a2a;
}
*{margin:0;padding:0;box-sizing:border-box}
html,body{width:1200px;height:881px;overflow:hidden;background:var(--backdrop)}
body{position:relative;font-family:"League Spartan",Arial,sans-serif;color:var(--text)}
.page{position:absolute;top:129px;width:441px;height:624px;background:var(--paper);overflow:hidden}
.page--cover{left:122px}
.page--terms{left:637px}

.brand{position:absolute;font-family:"League Spartan",Arial,sans-serif;font-weight:800;color:var(--ink);letter-spacing:4px;line-height:1;white-space:nowrap}

/* cover */
.cover-art{position:absolute;left:0;top:0;width:441px;height:624px}
.cover-brand{left:293px;top:45px;font-size:30px;letter-spacing:3px}
.cover-title{position:absolute;left:42px;top:64px;font-weight:700;font-size:49px;line-height:41px;color:var(--ink);letter-spacing:-.5px}
.cover-year{position:absolute;left:42px;top:149px;font-weight:600;font-size:27px;color:var(--red);line-height:1}
.cover-rule{position:absolute;left:41px;top:212px;width:237px;height:2px;background:var(--ink)}
.cover-subtitle{position:absolute;left:41px;top:236px;font-weight:600;font-size:14px;color:var(--red);line-height:1;white-space:nowrap}
.cover-intro{position:absolute;left:41px;top:257px;width:220px;font-size:6.8px;font-weight:600;line-height:7.1px;color:var(--ink)}

/* terms */
.header-bars{position:absolute;left:0;top:17px;width:441px;height:22px}
.terms-brand{left:363px;top:20px;font-size:17px;letter-spacing:2.5px}
.terms-title{position:absolute;left:25px;top:72px;font-weight:700;font-size:19px;line-height:1;color:var(--ink)}
.terms-title .accent{color:var(--red)}
.terms-body{position:absolute;left:24px;width:392px;font-size:9px;line-height:12px;color:var(--text);text-align:justify}
.terms-body--one{top:93px}
.terms-body--two{top:141px;height:72px;overflow:hidden}

.wheel{position:absolute;left:139px;top:223px;width:160px;height:160px}
.legend{position:absolute;display:flex;align-items:center;gap:5px;font-family:"Open Sans",Arial,sans-serif;font-size:5.6px;line-height:7.6px;color:var(--ink)}
.legend span{width:62px}
.legend svg{flex:none;width:14px;height:14px}
.legend--l1{left:38px;top:251px}.legend--l2{left:38px;top:296px}.legend--l3{left:38px;top:341px}
.legend--r1{left:322px;top:251px}.legend--r2{left:322px;top:296px}.legend--r3{left:322px;top:341px}

.notice{position:absolute;left:0;top:395px;width:441px;height:42px;background:var(--red);color:#fff;font-size:9px;line-height:12px;padding:3px 24px 0 24px}
.illustration{position:absolute;left:24px;top:438px;width:148px;height:117px;background:linear-gradient(160deg,#f4f4f4 0%,#e2e4e8 55%,#c9cfdb 100%)}
.side-text{position:absolute;left:181px;top:442px;width:231px;font-size:9px;line-height:12px;text-align:justify;color:var(--text)}
.side-text p+p{margin-top:12px}

.footer{position:absolute;left:0;top:596px;width:364px;height:16px;background:var(--charcoal);color:#fff;font-size:8.6px;line-height:16px;padding-left:27px;white-space:nowrap}
.corner{position:absolute;left:0;top:0;width:441px;height:624px;pointer-events:none}
</style>
</head>
<body>

<section class="page page--cover">
  <svg class="cover-art" viewBox="0 0 441 624">
    <defs>
      <linearGradient id="towerTones" x1="0" y1="0" x2="1" y2="1">
        <stop offset="0" stop-color="#c9dcee"/>
        <stop offset=".35" stop-color="#3b4656"/>
        <stop offset=".7" stop-color="#1b2230"/>
        <stop offset="1" stop-color="#6b4a2a"/>
      </linearGradient>
    </defs>
    <circle cx="485" cy="460" r="205" fill="var(--ink)"/>
    <circle cx="495" cy="460" r="205" fill="var(--red)"/>
    <circle cx="243" cy="618" r="187" fill="var(--ink)"/>
    <circle cx="252" cy="618" r="187" fill="var(--red)"/>
    <circle cx="420" cy="535" r="237" fill="var(--paper)"/>
    <circle cx="420" cy="535" r="230" fill="url(#towerTones)" role="img" aria-label="Photograph of glass office towers seen from below"/>
  </svg>
  <div class="brand cover-brand">ARVEN</div>
  <h1 class="cover-title">ANNUAL<br>REPORT</h1>
  <div class="cover-year">2022</div>
  <div class="cover-rule"></div>
  <h2 class="cover-subtitle">SANITARY INFRASTRUCTURE WORKS</h2>
  <p class="cover-intro">Lorem ipsum dolor sit amet, consectetuer adipiscing elit, sed diam nonummy nibh euismod tincidunt ut laoreet dolore magna aliquam erat volutpat. Ut wisi enim ad minim veniam, quis nostrud exerci tation ullamcorper suscipit lobortis nisl ut aliquip ex ea commodo consequat. Duis autem vel eum iriure dolor in hendrerit in vulputate velit esse molestie consequat, vel illum dolore eu feugiat nulla facilisis at vero eros et accumsan et iusto odio dignissim qui blandit praesent luptatum zzril delenit augue duis dolore</p>
</section>

<section class="page page--terms">
  <svg class="header-bars" viewBox="0 0 441 22">
    <rect x="-10" y="0" width="360" height="12" rx="6" fill="var(--red)"/>
    <rect x="-10" y="7" width="346" height="12" rx="6" fill="var(--ink)"/>
  </svg>
  <div class="brand terms-brand">ARVEN</div>

  <h2 class="terms-title"><span class="accent">TERMS &amp;</span> CONDITIONS</h2>
  <p class="terms-body terms-body--one">The pricing stated is valid for a period of forty-five (45) days from the date of the proposal. If not all required inform ation is received within ninety (90) days, we reserve the right to increase the pricing stated in this proposal.</p>
  <p class="terms-body terms-body--two">Payment is due within thirty (30) days of invoice receipt. There is a 1.5 percent (1.5%) finance charge on outstanding balances for each thirty (30) days, or portion thereof, overdue. If payment of our invoice(s) is not made within thirty (30) days, and we turn your account over to an attorney for collection, the client agrees to pay all costs of collection including, but not limited to, reasonable attorney's fees equal to 1/3 of the amount then remaining due. In addition, any account with an outstanding balance past sixty (60) days will have all work stopped until the account is made current. An additional fee may be</p>

  <svg class="wheel" viewBox="-80 -80 160 160" font-family="Open Sans, Arial, sans-serif" font-weight="600">
    <g stroke="var(--paper)" stroke-width="3">
      <path d="M0,-38 L0,-80 A80,80 0 0 1 69.3,-40 L32.9,-19 A38,38 0 0 0 0,-38Z" fill="var(--maroon)"/>
      <path d="M32.9,-19 L69.3,-40 A80,80 0 0 1 69.3,40 L32.9,19 A38,38 0 0 0 32.9,-19Z" fill="var(--charcoal)"/>
      <path d="M32.9,19 L69.3,40 A80,80 0 0 1 0,80 L0,38 A38,38 0 0 0 32.9,19Z" fill="var(--maroon)"/>
      <path d="M0,38 L0,80 A80,80 0 0 1 -69.3,40 L-32.9,19 A38,38 0 0 0 0,38Z" fill="var(--maroon)"/>
      <path d="M-32.9,19 L-69.3,40 A80,80 0 0 1 -69.3,-40 L-32.9,-19 A38,38 0 0 0 -32.9,19Z" fill="var(--charcoal)"/>
      <path d="M-32.9,-19 L-69.3,-40 A80,80 0 0 1 0,-80 L0,-38 A38,38 0 0 0 -32.9,-19Z" fill="var(--maroon)"/>
    </g>
    <circle r="37" fill="var(--ring)"/>
    <circle r="28" fill="var(--paper)"/>
    <path d="M-4,-14 L4,-14 L2,-10 C7,-7 8,-1 6,1 L-6,1 C-8,-1 -7,-7 -2,-10Z" fill="#555"/>
    <text x="0" y="-3" fill="#fff" font-size="6" text-anchor="middle">$</text>
    <text x="0" y="12" fill="var(--ink)" font-size="8" text-anchor="middle" font-weight="700">Goal</text>
    <g fill="#fff" font-size="9">
      <text transform="translate(32,-54) rotate(30)" text-anchor="middle">Object</text>
      <text transform="translate(64,0) rotate(90)" text-anchor="middle">Object</text>
      <text transform="translate(35,58) rotate(-30)" text-anchor="middle">Object</text>
      <text transform="translate(-33,58) rotate(30)" text-anchor="middle">Object</text>
      <text transform="translate(-60,0) rotate(-90)" text-anchor="middle">Object</text>
      <text transform="translate(-33,-50) rotate(-30)" text-anchor="middle">Object</text>
    </g>
    <g font-size="13" font-weight="700" text-anchor="middle">
      <text x="34" y="-29" fill="#9a9a9a">1</text>
      <text x="48" y="18" fill="#9a9a9a">2</text>
      <text x="10" y="55" fill="#fff">3</text>
      <text x="-37" y="40" fill="#9a9a9a">4</text>
      <text x="-48" y="-5" fill="#fff">5</text>
      <text x="-12" y="-44" fill="#fff">6</text>
    </g>
  </svg>

  <div class="legend legend--l1"><svg viewBox="0 0 14 14"><circle cx="7" cy="7" r="6" fill="none" stroke="var(--red)" stroke-width="1.5"/><text x="7" y="10" font-size="8" text-anchor="middle" fill="var(--red)" font-weight="700">$</text></svg><span>Lorem ipsum dolor sit amet, consectetur adipiscing elit</span></div>
  <div class="legend legend--l2"><svg viewBox="0 0 14 14"><circle cx="7" cy="6" r="5" fill="var(--ink)"/><circle cx="7" cy="6" r="2.5" fill="#fff"/><path d="M4,10 L3,14 L7,12 L11,14 L10,10Z" fill="var(--ink)"/></svg><span>Lorem ipsum dolor sit amet, consectetur adipiscing elit</span></div>
  <div class="legend legend--l3"><svg viewBox="0 0 14 14"><path d="M2,13 L2,5 M2,5 L0,7 M2,5 L4,7 M2,9 L10,3 M10,3 L7,3 M10,3 L10,6" stroke="var(--red)" stroke-width="1.6" fill="none"/></svg><span>Lorem ipsum dolor sit amet, consectetur adipiscing elit</span></div>
  <div class="legend legend--r1"><svg viewBox="0 0 14 14"><path d="M1,13 L13,13 M2,12 L12,5" stroke="var(--red)" stroke-width="1.3" fill="none"/><rect x="4" y="10" width="2" height="3" fill="var(--red)"/><rect x="7" y="9" width="2" height="4" fill="var(--red)"/><rect x="10" y="7" width="2" height="6" fill="var(--red)"/><text x="1" y="5" font-size="5" fill="var(--red)">$</text></svg><span>Lorem ipsum dolor sit amet, consectetur adipiscing elit</span></div>
  <div class="legend legend--r2"><svg viewBox="0 0 14 14"><path d="M1,1 L1,13 L13,13" stroke="var(--ink)" stroke-width="1.3" fill="none"/><rect x="3" y="9" width="2" height="3" fill="var(--ink)"/><rect x="6" y="7" width="2" height="5" fill="var(--ink)"/><rect x="9" y="5" width="2" height="7" fill="var(--ink)"/></svg><span>Lorem ipsum dolor sit amet, consectetur adipiscing elit</span></div>
  <div class="legend legend--r3"><svg viewBox="0 0 14 14"><path d="M1,5 L13,5 L9,9 L9,13 L5,13 L5,9Z" fill="var(--red)"/><circle cx="3" cy="2" r="1" fill="var(--red)"/><circle cx="7" cy="2" r="1" fill="var(--red)"/><circle cx="11" cy="2" r="1" fill="var(--red)"/></svg><span>Lorem ipsum dolor sit amet, consectetur adipiscing elit</span></div>

  <p class="notice">The pricing stated is valid for a period of forty-five (45) days from the date of the proposal. If not all required inform ation is received within ninety (90) days, we reserve the right to increase the pricing stated in this proposal.</p>

  <div class="illustration" role="img" aria-label="Illustration of two plumbers repairing wall pipes"></div>
  <div class="side-text">
    <p>The pricing stated is valid for a period of forty-five (45) days from the date of the proposal. If not all required inform ation is received within ninety (90) days, we reserve the right to increase the pricing stated in this proposal.</p>
    <p>Payment is due within thirty (30) days of invoice receipt. There is a 1.5 percent (1.5%) finance charge on outstanding balances for each thirty (30) days, or portion thereof,</p>
  </div>

  <div class="footer">48 Meridian Ave. Cedar Vale, NJ 07150 | P: 10-555-0142 | F: 732-555-0187</div>
  <svg class="corner" viewBox="0 0 441 624">
    <circle cx="409" cy="606" r="47" fill="var(--paper)"/>
    <circle cx="409" cy="606" r="44" fill="var(--red)"/>
    <circle cx="440" cy="592" r="49" fill="var(--red)" stroke="var(--paper)" stroke-width="1.5"/>
  </svg>
</section>

</body>
</html>
```